Bref créative
VORLAQ
Stationary Design
Simple
Tamer H. Bin Ruqail
Executive Director - Partner
P. O. Box 81726
Jeddah, 23847
Saudi Arabia
thruqail@vorlaq-mail.net
www.vorlaq-web.net
CR No. 7192836450
The CR should appear only on the stationary, and not on the business cards.
The stationary should be bilingual English and Arabic.
The Arabic text for the address information is as follows.
P. O. Box = ص. ب
Jeddah = جدة
Saudi Arabia = المملكة العربية السعودية
CR = س. ت
Numbers are the same in both languages.
I ask the designer to use best judgment in selecting the font to be used on the card.
The back of the business card, will mirror the front of it as it will be used for the Arabic information.
It will have the same information as listed above.

```html
<!DOCTYPE html>
<html lang="en">
<head>
<meta charset="utf-8">
<title>VORLAQ Stationery Set</title>
<link rel="stylesheet" href="https://fonts.googleapis.com/css2?family=Saira:wght@400;600;700&family=Noto+Kufi+Arabic:wght@400;600&display=swap">
<style>
  :root {
    --bg: #ece7e1;
    --paper: #ffffff;
    --red: #d2232a;
    --red-deep: #9e1219;
    --orange: #f26a21;
    --ink: #4a4a4a;
    --rule: #c9c9c9;
  }
  html, body { margin: 0; padding: 0; overflow: hidden; }
  body { width: 1200px; height: 422px; background: var(--bg); }
  .stationery-set { display: block; width: 1200px; height: 422px; }
  .brand-name { font-family: "Saira", sans-serif; font-weight: 700; fill: var(--red); letter-spacing: 1px; }
  .brand-name--light { fill: var(--paper); }
  .tagline { font-family: "Saira", sans-serif; font-weight: 400; fill: var(--ink); }
  .small-text { font-family: "Saira", sans-serif; font-weight: 400; fill: var(--ink); }
  .small-text--light { fill: var(--paper); }
  .arabic-text { font-family: "Noto Kufi Arabic", sans-serif; font-weight: 400; fill: var(--paper); }
  .label-text { font-family: "Saira", sans-serif; font-weight: 600; fill: var(--paper); }
  .field-label { font-family: "Saira", sans-serif; font-weight: 400; fill: var(--ink); }
  .sheet-shadow { fill: #000; opacity: .12; }
  .paper { fill: var(--paper); }
  .brand-mark { fill: var(--red); }
  .brand-mark--light { fill: var(--paper); }
  .field-box { fill: none; stroke: var(--rule); stroke-width: .8; }
  .field-line { stroke: var(--rule); stroke-width: .8; }
</style>
</head>
<body>
<svg class="stationery-set" viewBox="0 0 1200 422" xmlns="http://www.w3.org/2000/svg">
  <defs>
    <linearGradient id="red-sweep" x1="0" y1="0" x2="1" y2="0">
      <stop offset="0" stop-color="#9e1219"/>
      <stop offset=".55" stop-color="#d2232a"/>
      <stop offset="1" stop-color="#f26a21"/>
    </linearGradient>
    <radialGradient id="red-glow" cx=".55" cy=".45" r=".7">
      <stop offset="0" stop-color="#f7942a"/>
      <stop offset=".35" stop-color="#ee5a24"/>
      <stop offset=".8" stop-color="#d2232a"/>
      <stop offset="1" stop-color="#a3141c"/>
    </radialGradient>
    <clipPath id="card-back-clip"><rect x="93" y="94" width="50" height="28"/></clipPath>
  </defs>

  <!-- Business cards -->
  <g class="business-card business-card--front">
    <rect class="sheet-shadow" x="45" y="92" width="44" height="28"/>
    <rect class="paper" x="43" y="90" width="44" height="28"/>
    <path d="M43 110 Q65 100 87 104 L87 118 L43 118 Z" fill="url(#red-sweep)"/>
    <rect class="brand-mark" x="47" y="94" width="3.5" height="3.5"/>
    <text class="brand-name" x="52" y="97.5" font-size="4.2">VORLAQ</text>
  </g>
  <g class="business-card business-card--back">
    <rect class="sheet-shadow" x="95" y="96" width="50" height="28"/>
    <g clip-path="url(#card-back-clip)">
      <rect x="93" y="94" width="50" height="28" fill="url(#red-glow)"/>
      <path d="M93 94 L143 94 L143 100 Q118 96 93 106 Z" fill="var(--paper)"/>
    </g>
    <rect class="brand-mark--light" x="110" y="110.5" width="3.5" height="3.5"/>
    <text class="brand-name brand-name--light" x="115" y="114" font-size="4.2">VORLAQ</text>
  </g>

  <!-- Envelope -->
  <g class="envelope">
    <path d="M41 222 L150 176 L259 222 Z" fill="url(#red-sweep)"/>
    <rect class="sheet-shadow" x="44" y="224" width="218" height="150"/>
    <rect x="41" y="222" width="218" height="150" fill="url(#red-glow)"/>
    <path d="M41 222 L259 222 L259 300 Q170 262 41 318 Z" fill="var(--paper)"/>
    <rect class="brand-mark" x="52" y="232" width="7" height="7"/>
    <text class="brand-name" x="62" y="239" font-size="8">VORLAQ</text>
    <rect class="brand-mark--light" x="196" y="350" width="5" height="5"/>
    <text class="brand-name brand-name--light" x="204" y="355" font-size="6">VORLAQ</text>
  </g>

  <!-- Letterhead -->
  <g class="letterhead">
    <rect class="sheet-shadow" x="279" y="22" width="199" height="324"/>
    <rect class="paper" x="276" y="19" width="199" height="324"/>
    <rect class="brand-mark" x="288" y="32" width="9" height="9"/>
    <text class="brand-name" x="300" y="41" font-size="11">VORLAQ</text>
    <text class="tagline" x="300" y="47" font-size="3.5">Integrated Systems Solutions</text>
    <path d="M276 318 Q370 292 475 304 L475 343 L276 343 Z" fill="url(#red-sweep)"/>
    <path d="M276 314 Q370 288 475 300" fill="none" stroke="var(--orange)" stroke-width="1.5"/>
    <text class="small-text small-text--light" x="284" y="329" font-size="3.2">P. O. Box 81726 · Jeddah, 23847 · Saudi Arabia</text>
    <text class="small-text small-text--light" x="284" y="335" font-size="3.2">www.vorlaq-web.net · CR No. 7192836450</text>
    <text class="arabic-text" x="467" y="329" font-size="3.2" text-anchor="end">ص. ب 81726 · جدة 23847 · المملكة العربية السعودية</text>
    <text class="arabic-text" x="467" y="335" font-size="3.2" text-anchor="end">س. ت 7192836450</text>
  </g>

  <!-- Fax sheet -->
  <g class="fax-sheet">
    <rect class="sheet-shadow" x="500" y="22" width="199" height="324"/>
    <rect class="paper" x="497" y="19" width="199" height="324"/>
    <rect class="brand-mark" x="509" y="32" width="9" height="9"/>
    <text class="brand-name" x="521" y="41" font-size="11">VORLAQ</text>
    <rect x="590" y="78" width="60" height="8" fill="var(--red)"/>
    <text class="label-text" x="645" y="84" font-size="5" text-anchor="end">FAX</text>
    <g class="fax-fields">
      <rect x="513" y="94" width="14" height="7" fill="var(--red)"/>
      <text class="label-text" x="520" y="99.2" font-size="3.6" text-anchor="middle">To</text>
      <text class="field-label" x="533" y="99" font-size="3.6">Name:</text>
      <line class="field-line" x1="548" y1="100" x2="675" y2="100"/>
      <text class="field-label" x="533" y="109" font-size="3.6">Fax:</text>
      <line class="field-line" x1="548" y1="110" x2="675" y2="110"/>
      <rect x="513" y="128" width="14" height="7" fill="var(--red)"/>
      <text class="label-text" x="520" y="133.2" font-size="3.6" text-anchor="middle">From</text>
      <text class="field-label" x="533" y="133" font-size="3.6">Name:</text>
      <line class="field-line" x1="548" y1="134" x2="675" y2="134"/>
      <text class="field-label" x="533" y="143" font-size="3.6">Date:</text>
      <line class="field-line" x1="548" y1="144" x2="675" y2="144"/>
      <text class="field-label" x="533" y="153" font-size="3.6">Pages:</text>
      <line class="field-line" x1="548" y1="154" x2="675" y2="154"/>
      <rect x="513" y="168" width="14" height="7" fill="var(--red)"/>
      <text class="label-text" x="520" y="173" font-size="3.2" text-anchor="middle">Subject</text>
      <rect class="field-box" x="533" y="168" width="142" height="58"/>
    </g>
    <path d="M497 318 Q590 292 696 304 L696 343 L497 343 Z" fill="url(#red-sweep)"/>
    <path d="M497 314 Q590 288 696 300" fill="none" stroke="var(--orange)" stroke-width="1.5"/>
    <text class="small-text small-text--light" x="505" y="329" font-size="3.2">P. O. Box 81726 · Jeddah, 23847 · Saudi Arabia</text>
    <text class="small-text small-text--light" x="505" y="335" font-size="3.2">www.vorlaq-web.net · CR No. 7192836450</text>
    <text class="arabic-text" x="688" y="329" font-size="3.2" text-anchor="end">ص. ب 81726 · جدة 23847 · المملكة العربية السعودية</text>
    <text class="arabic-text" x="688" y="335" font-size="3.2" text-anchor="end">س. ت 7192836450</text>
  </g>

  <!-- Presentation folder -->
  <g class="folder">
    <rect class="sheet-shadow" x="740" y="22" width="451" height="389"/>
    <rect x="737" y="19" width="226" height="389" fill="url(#red-glow)"/>
    <rect x="963" y="19" width="225" height="389" fill="url(#red-glow)"/>
    <line x1="963" y1="19" x2="963" y2="408" stroke="var(--red-deep)" stroke-width="1"/>
    <path d="M963 19 L1188 19 L1188 92 Q1080 60 963 96 Z" fill="var(--paper)"/>
    <rect class="brand-mark" x="1108" y="32" width="12" height="12"/>
    <text class="brand-name" x="1124" y="44" font-size="13">VORLAQ</text>
    <text class="tagline" x="1124" y="51" font-size="4">Integrated Systems Solutions</text>
    <text class="small-text small-text--light" x="1075" y="255" font-size="3.6" text-anchor="middle">P. O. Box 81726 · Jeddah, 23847</text>
    <text class="small-text small-text--light" x="1075" y="261" font-size="3.6" text-anchor="middle">www.vorlaq-web.net</text>
    <g class="folder-pocket">
      <path d="M737 340 Q850 318 963 332 L963 408 L737 408 Z" fill="var(--red-deep)" opacity=".35"/>
      <path d="M737 344 Q850 322 963 336" fill="none" stroke="var(--paper)" stroke-width="2"/>
      <rect class="paper" x="860" y="360" width="46" height="26" transform="rotate(-8 883 373)"/>
      <rect class="brand-mark" x="866" y="366" width="4" height="4" transform="rotate(-8 883 373)"/>
      <text class="brand-name" x="872" y="370" font-size="4.5" transform="rotate(-8 883 373)">VORLAQ</text>
    </g>
  </g>
</svg>
</body>
</html>
```